Manuka Honey company needs a Upmarket, Luxury Website!

New Zealand, Taranaki based Manuka Honey company Marumaru Honey is looking for a new website, we are looking for an upmarket, luxury, serious website design. We export the highest quality quality Manuka Honey, straight from the Taranaki region.

Main export markets are Asia & Europe, also New Zealand & Australia.

Looking to have a beautiful, upmarket, serious, luxurious & graphical experience with mobile optimization in mind. Like the use of product staging/mockups

You can use copy from other websites to build the site and we will change the copy after the design is finished.

***Please include 'Honey Product' mockups in website.

*Will add illustrator files in coming days***

Feel free to make website functional in Shopify, Wordpress or WIX

Target Market(s)

Asia, Europe (main markets) New Zealand, Australia (Submarkets)

Coding

Coded - Design and coding required

Number of Pages Required

4 page

Requirements
Must have
• Home, Shop, About Us, Contact Us

Homepage to include:

Our Products
Company Video (video under construction)
What is MGO/UMF
Newsletter Opt-in

***(Not in Order)***

Please include 'Honey Product' mockups in website.
*Will add illustrator files in coming days
Nice to have
• FAQ & Partnership Inquiries (hyperlink in footer)

```html
<!DOCTYPE html>
<html lang="en">
<head>
<meta charset="utf-8">
<title>Marumaru Honey — Taranaki Manuka Honey</title>
<link href="https://fonts.googleapis.com/css2?family=Poppins:wght@400;500;600;700;800&display=swap" rel="stylesheet">
<style>
:root{
  --page:#f9f9fc;
  --panel:#f3f3f5;
  --ink:#222222;
  --text:#555555;
  --muted:#888888;
  --gold:#c9a64f;
  --gold-light:#f6ef9c;
  --gold-deep:#c4a352;
  --green:#6a9a1a;
  --leaf:#2f5a22;
  --dark:#2b2b2b;
  --line:#e6e6ea;
}
*{box-sizing:border-box;margin:0;padding:0}
html,body{width:1200px;height:4172px;overflow:hidden}
body{position:relative;background:var(--page);font-family:'Poppins',sans-serif;color:var(--ink)}
.abs{position:absolute}
a{color:inherit;text-decoration:none}

/* header */
.header-panel{left:567px;top:0;width:633px;height:534px;background:var(--panel)}
.brand{left:88px;top:25px;width:100px;height:100px;border:2px solid #bbb;border-radius:50%;display:flex;align-items:center;justify-content:center;text-align:center;font-weight:700;font-size:12px;line-height:1.2;color:var(--ink)}
.nav{top:66px;left:662px;font-size:13px;font-weight:500;color:var(--ink)}
.nav a{position:absolute;white-space:nowrap}
.icons{left:1015px;top:62px;display:flex;gap:12px}
.icons svg{width:20px;height:20px;stroke:var(--ink);fill:none;stroke-width:1.6}
.cart-badge{position:absolute;right:-7px;top:-4px;width:12px;height:12px;border-radius:50%;background:var(--gold);font-size:8px;display:flex;align-items:center;justify-content:center;color:#222}

/* hero */
.eyebrow{left:87px;top:238px;font-size:15px;font-weight:600}
.hero-title{left:87px;top:262px;font-size:46px;font-weight:800;line-height:45px;letter-spacing:.5px}
.hero-copy{left:87px;top:414px;font-size:14px;line-height:23px;color:var(--text);width:360px}
.btn-gold{left:87px;top:481px;width:140px;height:45px;border-radius:23px;background:linear-gradient(90deg,var(--gold-light),var(--gold));font-size:13px;font-weight:700;display:flex;align-items:center;justify-content:center}
.vline{width:2px;background:linear-gradient(var(--gold-light),var(--gold))}

/* about */
.gold-band{left:0;top:810px;width:1200px;height:607px;background:linear-gradient(100deg,var(--gold-light) 0%,#e9d98a 45%,var(--gold-deep) 100%)}
.leaf-area{background:linear-gradient(160deg,rgba(47,90,34,.55),rgba(18,48,20,.35))}
.frame{background:#fff;box-shadow:0 10px 30px rgba(0,0,0,.12)}
.about-card{left:559px;top:931px;width:552px;height:369px;background:#fff}
.section-h{font-weight:600;color:var(--ink);white-space:nowrap}
.about-card h2{position:absolute;left:59px;top:52px;font-size:36px}
.rule{height:2px;background:#cfcfcf}
.about-card p{position:absolute;left:59px;top:128px;width:450px;font-size:13.5px;line-height:20.5px;color:var(--text)}
.btn-grey{left:59px;top:270px;width:127px;height:38px;border-radius:19px;background:#ececee;font-size:13px;font-weight:600;display:flex;align-items:center;justify-content:center}

/* products */
.products-title{left:0;width:1200px;top:1624px;text-align:center;font-size:47px;font-weight:700}
.card{top:1773px;width:238px;height:283px;background:#fff;box-shadow:0 6px 20px rgba(0,0,0,.06)}
.product-shot{position:absolute;top:-65px;left:69px;width:100px;height:186px;background:linear-gradient(180deg,#e6b84a,#d9a232)}
.card h3{position:absolute;top:145px;left:0;width:100%;text-align:center;font-size:16px;font-weight:600;line-height:22px}
.stars{position:absolute;top:194px;left:0;width:100%;display:flex;justify-content:center;gap:2px}
.stars svg{width:16px;height:16px}
.card hr{position:absolute;top:235px;left:14px;width:210px;border:0;border-top:1px solid var(--line)}
.price{position:absolute;top:247px;left:0;width:100%;text-align:center;font-size:14px;font-weight:500}
.price b{color:var(--green);font-size:19px;font-weight:700}

/* mgo */
.mgo-title{left:0;width:1200px;top:2154px;text-align:center;font-size:46px;font-weight:700}
.vs{left:131px;top:2349px;width:78px;height:78px;border-radius:50%;background:linear-gradient(135deg,#f2e58c,var(--gold));color:#fff;font-size:28px;font-weight:700;display:flex;align-items:center;justify-content:center}
.mgo-card{left:87px;top:2399px;width:583px;height:366px;background:#fff;box-shadow:0 10px 30px rgba(0,0,0,.08)}
.mgo-card h3{position:absolute;left:44px;top:64px;font-size:22px;font-weight:500}
.mgo-card p{position:absolute;left:44px;top:105px;width:490px;font-size:13.5px;line-height:21px;color:var(--text)}
.ratings{position:absolute;left:44px;top:164px;width:322px;border-collapse:collapse;font-size:13.5px;font-weight:500}
.ratings td{height:34px;border-bottom:1px solid var(--line)}
.ratings tr:last-child td{border-bottom:0}
.ratings td:first-child{width:160px}
.arrow-btn{width:44px;height:44px;border-radius:50%;border:1.5px solid #bbb;display:flex;align-items:center;justify-content:center;background:var(--page)}
.arrow-btn svg{width:18px;height:18px;stroke:#777;fill:none;stroke-width:1.6}

/* video */
.play{left:518px;top:3248px;width:100px;height:100px;border-radius:50%;background:linear-gradient(135deg,#e8d77a,var(--gold));display:flex;align-items:center;justify-content:center}
.video-title{left:652px;top:3180px;font-size:36px}
.video-copy{left:653px;width:465px;font-size:14px;line-height:22px;color:var(--text)}

/* newsletter + footer */
.footer{left:0;top:3732px;width:1200px;height:440px;background:var(--dark)}
.newsletter{left:594px;top:3656px;width:606px;height:149px;background:linear-gradient(100deg,#f3e8a0,#d6b964 60%,#c9a64f)}
.newsletter h4{position:absolute;left:36px;top:38px;font-size:11px;font-weight:600}
.subscribe{position:absolute;left:36px;top:64px;width:479px;height:46px;background:#fff;display:flex;align-items:center}
.subscribe span{margin-left:40px;font-size:14px;color:#999}
.subscribe svg{position:absolute;left:16px;top:16px;width:16px;height:14px;fill:#999}
.subscribe b{position:absolute;right:5px;top:5px;width:115px;height:36px;background:#1f1f1f;color:#fff;font-size:11px;font-weight:700;display:flex;align-items:center;justify-content:center}
.foot-brand{left:215px;top:3884px;width:140px;height:140px;border-radius:50%;border:2px solid var(--gold);display:flex;align-items:center;justify-content:center;text-align:center;color:#fff;font-size:17px;font-weight:600;line-height:1.3}
.foot-col h5{font-size:16px;font-weight:600;color:#fff;margin-bottom:14px}
.foot-col a{display:block;font-size:13px;color:#e8e8e8}
.social{top:3913px;width:36px;height:36px;border-radius:50%;background:#444}
.copyright{left:0;width:1200px;top:4136px;text-align:center;font-size:11px;font-weight:500;color:#ddd}
.foot-rule{left:0;top:4120px;width:1200px;border-top:1px solid #3a3a3a}
.to-top{left:1128px;top:4091px;width:42px;height:42px;border-radius:50%;background:linear-gradient(135deg,#f2e58c,var(--gold));display:flex;align-items:center;justify-content:center}
.to-top svg{width:16px;height:16px;stroke:#333;fill:none;stroke-width:1.6}
</style>
</head>
<body>

<!-- header -->
<div class="abs header-panel"></div>
<div class="abs brand">MARUMARU<br>HONEY</div>
<nav class="abs nav">
  <a style="left:0">HOME</a>
  <a style="left:67px">SHOP</a>
  <a style="left:130px">ABOUT US</a>
  <a style="left:224px">CONTACT US</a>
</nav>
<div class="abs icons">
  <svg viewBox="0 0 20 20"><circle cx="10" cy="6" r="4"/><path d="M3 19c0-4 3-7 7-7s7 3 7 7"/></svg>
  <svg viewBox="0 0 20 20"><circle cx="8.5" cy="8.5" r="6"/><path d="M13 13l5 5"/></svg>
  <span style="position:relative"><svg viewBox="0 0 20 20"><path d="M1 3h3l2.5 10h10l2-7H5.5"/><circle cx="8" cy="17" r="1.3"/><circle cx="15" cy="17" r="1.3"/></svg><span class="cart-badge">0</span></span>
</div>

<!-- hero -->
<div class="abs eyebrow">New Zealand</div>
<h1 class="abs hero-title">Taranaki<br>based manuka<br>honey...</h1>
<p class="abs hero-copy">Export the highest quality quality Manuka Honey, straight from the Taranaki region.</p>
<a class="abs btn-gold">SHOP NOW</a>
<div class="abs vline" style="left:325px;top:567px;height:166px"></div>
<div class="abs" role="img" aria-label="Beekeeper in a white suit lifting a frame from a hive in the forest" style="left:482px;top:133px;width:451px;height:534px;background:linear-gradient(160deg,#5d6a50,#b9b7a8 55%,#6f6c5c)"></div>

<!-- about -->
<div class="abs gold-band"></div>
<div class="abs leaf-area" role="img" aria-label="Decorative palm leaf" style="left:495px;top:737px;width:220px;height:600px"></div>
<div class="abs frame" style="left:87px;top:931px;width:408px;height:567px"></div>
<div class="abs" role="img" aria-label="Two beekeepers tending hives under tall trees" style="left:102px;top:949px;width:380px;height:539px;background:linear-gradient(170deg,#3c8fb4 0%,#7a6a48 40%,#34503f 75%,#2c3a34)"></div>
<section class="abs about-card">
  <h2 class="section-h">About Marumaru Honey</h2>
  <div class="abs rule" style="left:40px;top:105px;width:65px"></div>
  <p>Aenean sollicitudin, lorem quis bibendum auctor, nisi elit consequat ipsum, nec sagittis sem nibh id elit. Duis sed odio sit amet nibh vulputate cursus a sit amet mauris. Morbi accumsan ipsum velit. Nam nec tellus a odio tincidunt auctor a ornare odio. Sed non&nbsp; mauris vitae erat consequat auctor eu in elit. Class aptent taciti sociosqu ad litora...</p>
  <a class="abs btn-grey">READ MORE</a>
</section>

<!-- products -->
<div class="abs vline" style="left:834px;top:1473px;height:167px"></div>
<h2 class="abs products-title">Our Products</h2>

<div class="abs card" style="left:104px">
  <div class="product-shot" role="img" aria-label="Product photo of a manuka honey jar"></div>
  <h3>01: Some product<br>heading goes here</h3>
  <div class="stars"><svg viewBox="0 0 20 20"><path fill="#e7cf6a" d="M10 1l2.7 6 6.3.6-4.8 4.3 1.4 6.4L10 15l-5.6 3.3 1.4-6.4L1 7.6 7.3 7z"/></svg><svg viewBox="0 0 20 20"><path fill="#e7cf6a" d="M10 1l2.7 6 6.3.6-4.8 4.3 1.4 6.4L10 15l-5.6 3.3 1.4-6.4L1 7.6 7.3 7z"/></svg><svg viewBox="0 0 20 20"><path fill="#e7cf6a" d="M10 1l2.7 6 6.3.6-4.8 4.3 1.4 6.4L10 15l-5.6 3.3 1.4-6.4L1 7.6 7.3 7z"/></svg><svg viewBox="0 0 20 20"><path fill="#e7cf6a" d="M10 1l2.7 6 6.3.6-4.8 4.3 1.4 6.4L10 15l-5.6 3.3 1.4-6.4L1 7.6 7.3 7z"/></svg><svg viewBox="0 0 20 20"><path fill="#f4ebbd" d="M10 1l2.7 6 6.3.6-4.8 4.3 1.4 6.4L10 15l-5.6 3.3 1.4-6.4L1 7.6 7.3 7z"/></svg></div>
  <hr><div class="price">Price: <b>$25.00</b></div>
</div>
<div class="abs card" style="left:355px">
  <div class="product-shot" role="img" aria-label="Product photo of a manuka honey jar"></div>
  <h3>01: Some product<br>heading goes here</h3>
  <div class="stars"><svg viewBox="0 0 20 20"><path fill="#e7cf6a" d="M10 1l2.7 6 6.3.6-4.8 4.3 1.4 6.4L10 15l-5.6 3.3 1.4-6.4L1 7.6 7.3 7z"/></svg><svg viewBox="0 0 20 20"><path fill="#e7cf6a" d="M10 1l2.7 6 6.3.6-4.8 4.3 1.4 6.4L10 15l-5.6 3.3 1.4-6.4L1 7.6 7.3 7z"/></svg><svg viewBox="0 0 20 20"><path fill="#e7cf6a" d="M10 1l2.7 6 6.3.6-4.8 4.3 1.4 6.4L10 15l-5.6 3.3 1.4-6.4L1 7.6 7.3 7z"/></svg><svg viewBox="0 0 20 20"><path fill="#e7cf6a" d="M10 1l2.7 6 6.3.6-4.8 4.3 1.4 6.4L10 15l-5.6 3.3 1.4-6.4L1 7.6 7.3 7z"/></svg><svg viewBox="0 0 20 20"><path fill="#f4ebbd" d="M10 1l2.7 6 6.3.6-4.8 4.3 1.4 6.4L10 15l-5.6 3.3 1.4-6.4L1 7.6 7.3 7z"/></svg></div>
  <hr><div class="price">Price: <b>$25.00</b></div>
</div>
<div class="abs card" style="left:607px">
  <div class="product-shot" role="img" aria-label="Product photo of a manuka honey jar"></div>
  <h3>01: Some product<br>heading goes here</h3>
  <div class="stars"><svg viewBox="0 0 20 20"><path fill="#f4ebbd" d="M10 1l2.7 6 6.3.6-4.8 4.3 1.4 6.4L10 15l-5.6 3.3 1.4-6.4L1 7.6 7.3 7z"/></svg><svg viewBox="0 0 20 20"><path fill="#f4ebbd" d="M10 1l2.7 6 6.3.6-4.8 4.3 1.4 6.4L10 15l-5.6 3.3 1.4-6.4L1 7.6 7.3 7z"/></svg><svg viewBox="0 0 20 20"><path fill="#f4ebbd" d="M10 1l2.7 6 6.3.6-4.8 4.3 1.4 6.4L10 15l-5.6 3.3 1.4-6.4L1 7.6 7.3 7z"/></svg><svg viewBox="0 0 20 20"><path fill="#f4ebbd" d="M10 1l2.7 6 6.3.6-4.8 4.3 1.4 6.4L10 15l-5.6 3.3 1.4-6.4L1 7.6 7.3 7z"/></svg><svg viewBox="0 0 20 20"><path fill="#f4ebbd" d="M10 1l2.7 6 6.3.6-4.8 4.3 1.4 6.4L10 15l-5.6 3.3 1.4-6.4L1 7.6 7.3 7z"/></svg></div>
  <hr><div class="price">Price: <b>$25.00</b></div>
</div>
<div class="abs card" style="left:858px">
  <div class="product-shot" role="img" aria-label="Product photo of a manuka honey jar"></div>
  <h3>01: Some product<br>heading goes here</h3>
  <div class="stars"><svg viewBox="0 0 20 20"><path fill="#e7cf6a" d="M10 1l2.7 6 6.3.6-4.8 4.3 1.4 6.4L10 15l-5.6 3.3 1.4-6.4L1 7.6 7.3 7z"/></svg><svg viewBox="0 0 20 20"><path fill="#e7cf6a" d="M10 1l2.7 6 6.3.6-4.8 4.3 1.4 6.4L10 15l-5.6 3.3 1.4-6.4L1 7.6 7.3 7z"/></svg><svg viewBox="0 0 20 20"><path fill="#e7cf6a" d="M10 1l2.7 6 6.3.6-4.8 4.3 1.4 6.4L10 15l-5.6 3.3 1.4-6.4L1 7.6 7.3 7z"/></svg><svg viewBox="0 0 20 20"><path fill="#e7cf6a" d="M10 1l2.7 6 6.3.6-4.8 4.3 1.4 6.4L10 15l-5.6 3.3 1.4-6.4L1 7.6 7.3 7z"/></svg><svg viewBox="0 0 20 20"><path fill="#f4ebbd" d="M10 1l2.7 6 6.3.6-4.8 4.3 1.4 6.4L10 15l-5.6 3.3 1.4-6.4L1 7.6 7.3 7z"/></svg></div>
  <hr><div class="price">Price: <b>$25.00</b></div>
</div>

<!-- mgo / umf -->
<div class="abs vline" style="left:325px;top:2137px;height:162px"></div>
<h2 class="abs mgo-title">What is MGO/UMF</h2>
<div class="abs leaf-area" role="img" aria-label="Decorative palm leaf" style="left:830px;top:2740px;width:370px;height:320px"></div>
<div class="abs" role="img" aria-label="Honey jar and wooden dipper on a rustic wooden table" style="left:599px;top:2263px;width:512px;height:616px;background:linear-gradient(150deg,#6d5a44,#b88a3a 40%,#8a6a48 70%,#5a4a38)"></div>
<section class="abs mgo-card">
  <h3>How the ratings comapare UMF vs MGO</h3>
  <p>Aenean sollicitudin, lorem quis bibendum auctor, nisi elit consequat ipsum, nec sagittis sem nibh id elit..</p>
  <table class="ratings">
    <tr><td>UMF 05</td><td>MGO89</td></tr>
    <tr><td>UMF 10</td><td>MGO263</td></tr>
    <tr><td>UMF 15</td><td>MGO514</td></tr>
    <tr><td>UMF 20</td><td>MGO829</td></tr>
    <tr><td>UMF 25</td><td>MGO1200</td></tr>
  </table>
</section>
<div class="abs vs">VS</div>
<div class="abs" style="left:205px;top:2858px;width:280px;border-top:1px solid #ccc"></div>
<div class="abs arrow-btn" style="left:161px;top:2836px"><svg viewBox="0 0 20 20"><path d="M16 10H4M9 5l-5 5 5 5"/></svg></div>
<div class="abs arrow-btn" style="left:485px;top:2836px"><svg viewBox="0 0 20 20"><path d="M4 10h12M11 5l5 5-5 5"/></svg></div>

<!-- video -->
<div class="abs" role="img" aria-label="Gloved hands lifting a honeycomb frame from a hive box" style="left:175px;top:3040px;width:395px;height:470px;background:linear-gradient(150deg,#7a6040,#b9915a 45%,#d9cdb8 80%)"></div>
<div class="abs frame" style="left:86px;top:3311px;width:273px;height:286px"></div>
<div class="abs" role="img" aria-label="Beekeeper in a white suit inspecting a hive" style="left:96px;top:3322px;width:254px;height:266px;background:linear-gradient(160deg,#3f5a2f,#9ea290 50%,#e4e2da)"></div>
<div class="abs play"><svg width="26" height="28" viewBox="0 0 26 28"><path d="M4 2l20 12L4 26z" fill="#333"/></svg></div>
<h2 class="abs video-title section-h">Marumaru Honey video</h2>
<div class="abs rule" style="left:652px;top:3236px;width:65px"></div>
<p class="abs video-copy" style="top:3259px">Aenean sollicitudin, lorem quis bibendum auctor, nisi elit amet nibh vulputate cursus a sit amet mauris cumsan ipsum velit. Nam nec tellus a odio tincidunt auctor a ornare odio. Sed non&nbsp; mauris vitae...</p>
<p class="abs video-copy" style="top:3371px">Litora torquent per conubia nostra, per inceptos himenaeos. Mauris in erat justo. Nullam ac urna eu felis dapibus mentum sit amet a augue.</p>

<!-- footer -->
<footer class="abs footer"></footer>
<section class="abs newsletter">
  <h4>JOIN OUR MAILING LIST</h4>
  <div class="subscribe">
    <svg viewBox="0 0 16 14"><path d="M0 1h16v12H0z M0 1l8 6 8-6"/></svg>
    <span>Enter your email address</span>
    <b>SUBSCRIBE</b>
  </div>
</section>
<div class="abs foot-brand">MARUMARU<br>HONEY</div>
<div class="abs foot-col" style="left:439px;top:3874px">
  <h5>Information</h5>
  <a style="margin-bottom:10px">About us</a>
  <a style="margin-bottom:8px">FAQ</a>
  <a>Partnership Inquiries</a>
</div>
<div class="abs foot-col" style="left:664px;top:3874px">
  <h5>Let us help</h5>
  <a style="margin-bottom:11px">Privacy Policy</a>
  <a style="margin-bottom:11px">Return Policy</a>
  <a style="margin-bottom:11px">Terms &amp; Condition</a>
  <a style="margin-bottom:11px">Contact us</a>
  <a>FAQ's</a>
</div>
<div class="abs foot-col" style="left:869px;top:3874px"><h5>Follow Us</h5></div>
<div class="abs social" style="left:866px"></div>
<div class="abs social" style="left:908px"></div>
<div class="abs social" style="left:950px"></div>
<div class="abs social" style="left:993px"></div>
<div class="abs foot-rule"></div>
<div class="abs to-top"><svg viewBox="0 0 16 16"><path d="M8 14V2M3 7l5-5 5 5"/></svg></div>
<div class="abs copyright">©2021 ABOUT MARUMARU HONEY. ALL RIGHTS RESERVED</div>

</body>
</html>
```